Fantasy Sports Website re-Design

We need a website designed for our fantasy sports website. The website is TorvexPlay.com . An example of the website layout would be like : https://www.quandrel.com/fantasy-sports/fantasy-sports-solutions. We like this site, because of the screenshots on 1 side and a description on the other side. This layout style will showcase the features we have on our site. Somewhere in the header there will be a video explaining what the site is. We would like the style to be black and gold. Like a casino. Attached is an example logo to give the style we want.

Target Market(s)

fantasy sports

Number of Pages Required

3 page

Colors
fecb35
000000

Requirements
Must have
• mockups of index page
Nice to have
• mockups of sub pages

```html
<!DOCTYPE html>
<html lang="en">
<head>
<meta charset="utf-8">
<title>TorvexPlay.com – Lobby</title>
<link href="https://fonts.googleapis.com/css2?family=Barlow+Condensed:ital,wght@0,400;0,500;0,600;0,700;1,700&display=swap" rel="stylesheet">
<style>
:root{
  --gold:#fecb35;
  --black:#000000;
  --header:#141414;
  --subnav:#efefef;
  --panel:#1a1a1a;
  --chip:#2b2b2b;
  --chip-dim:#8a8a8a;
  --white:#ffffff;
  --ink:#222222;
  --rule:#e6e6e6;
  --green:#5aa52b;
  --green-soft:#e9f3df;
  --green-text:#7ab842;
  --red:#ec3a55;
}
*{box-sizing:border-box;margin:0;padding:0}
html,body{width:765px;height:1200px;overflow:hidden;background:var(--black)}
body{position:relative;font-family:"Barlow Condensed",sans-serif;color:var(--white)}
.site-header{position:absolute;left:0;top:0;width:765px;height:46px;background:var(--header)}
.brand{position:absolute;left:57px;top:12px;font-size:20px;font-weight:700;color:var(--gold);letter-spacing:1px;line-height:22px}
.main-nav{position:absolute;top:17px;font-size:10px;font-weight:400;color:var(--white);white-space:nowrap}
.btn-outline{position:absolute;top:12px;height:22px;width:55px;border:1.5px solid var(--white);font-size:9.5px;font-weight:400;display:flex;align-items:center;justify-content:center;gap:6px}
.btn-outline.gold{border-color:var(--gold);color:var(--gold)}
.sub-nav{position:absolute;left:0;top:46px;width:765px;height:30px;background:var(--subnav)}
.sub-nav span{position:absolute;top:9px;font-size:9.5px;font-weight:400;color:var(--ink);white-space:nowrap}
.sub-nav .current{color:#888}
.sub-nav .current::after{content:"";position:absolute;left:0;right:0;top:20px;height:2px;background:var(--gold)}
.stadium{position:absolute;left:0;top:380px;width:765px;height:720px;background:radial-gradient(ellipse 70% 50% at 50% 50%,#2b3a1c 0%,#16200f 45%,#000 85%)}
.page-title{position:absolute;left:56px;top:130px;font-size:27px;font-weight:700;font-style:italic}
.page-title::after{content:"";position:absolute;left:1px;top:37px;width:28px;height:2px;background:var(--gold)}
.countdown-label{position:absolute;left:283px;top:122px;width:200px;text-align:center;font-size:11px;font-weight:700;font-style:italic}
.count-box{position:absolute;top:143px;width:34px;height:39px;background:#1d1d1d;border-radius:2px;font-size:18px;font-weight:700;font-style:italic;display:flex;align-items:center;justify-content:center}
.colon{position:absolute;top:155px;width:4px}
.colon i{display:block;width:3px;height:3px;border-radius:50%;border:1px solid var(--gold);margin-bottom:4px}
.create-btn{position:absolute;left:625px;top:142px;width:83px;height:22px;background:var(--green);font-size:9px;font-weight:400;display:flex;align-items:center;justify-content:center;gap:7px}
.filter{position:absolute;left:57px;top:213px;width:157px;height:908px;background:var(--panel)}
.filter-title{position:absolute;left:14px;top:26px;font-size:14px;font-weight:700;font-style:italic}
.rule{position:absolute;left:14px;width:128px;height:1px;background:#cfcfcf}
.search{position:absolute;left:14px;top:59px;width:128px;height:22px;border:1px solid #3a3a3a;font-size:8.5px;font-weight:400;display:flex;align-items:center;padding-left:6px;gap:4px}
.chip-grid{position:absolute;left:14px;top:88px;width:128px;display:grid;grid-template-columns:61px 61px;column-gap:6px;row-gap:6.3px}
.chip{height:22px;background:var(--chip);font-size:8px;font-weight:600;display:flex;align-items:center;justify-content:center;text-transform:uppercase;white-space:nowrap}
.chip.dim{color:var(--chip-dim)}
.chip.on{background:var(--gold);color:var(--ink)}
.stack{position:absolute;left:14px;width:128px;display:flex;flex-direction:column;gap:6.3px}
.stack .chip{height:22.5px}
.fee-label{position:absolute;left:14px;top:604px;font-size:8.5px;font-weight:600}
.fee-input{position:absolute;top:619px;width:61px;height:22px;background:var(--chip);font-size:8.5px;display:flex;align-items:center;justify-content:center}
.dash{position:absolute;left:77px;top:624px;font-size:9px}
.slider{position:absolute;left:14px;top:649px;width:128px;height:14px}
.contests{position:absolute;left:225px;top:213px;width:483px;height:680px;background:var(--white);color:var(--ink)}
.th{position:absolute;top:18px;font-size:8px;font-weight:400;display:flex;align-items:center;gap:3px;white-space:nowrap}
.badge{display:inline-flex;width:11px;height:11px;border-radius:50%;background:var(--gold);font-size:6.5px;font-weight:700;align-items:center;justify-content:center}
.head-rule{position:absolute;left:18px;top:35px;width:449px;height:1px;background:var(--rule)}
.rows{position:absolute;left:0;top:43px}
.row{position:absolute;left:18px;width:449px;height:37.4px;border-bottom:1px solid var(--rule)}
.row.last{border-bottom:none}
.row span{position:absolute;top:12.5px;font-size:8.8px;font-weight:400;white-space:nowrap}
.row .name{left:12px;top:10.5px;font-size:10.5px;font-weight:500}
.row svg{position:absolute;left:1px;top:14px}
.btn{position:absolute;top:7px;height:22px;width:35px;background:var(--green-soft);color:var(--green-text);font-size:8.8px;font-weight:400;display:flex;align-items:center;justify-content:center}
.btn.full{background:var(--red);color:var(--white)}
.footer-rule{position:absolute;left:0;top:1160px;width:765px;height:1px;background:#1e1e1e}
.footer{position:absolute;left:0;top:1174px;width:765px;text-align:center;font-size:8.5px;font-weight:500}
</style>
</head>
<body>
<header class="site-header">
  <div class="brand">TORVEX PLAY</div>
  <span class="main-nav" style="left:359px">Powered by Stakewell.com</span>
  <span class="main-nav" style="left:464px">Site-Wide Activity</span>
  <span class="main-nav" style="left:541px">Members</span>
  <div class="btn-outline" style="left:591px">Signup <svg width="7" height="6" viewBox="0 0 7 6"><path d="M0 3h6M4 1l2 2-2 2" stroke="#fff" fill="none"/></svg></div>
  <div class="btn-outline gold" style="left:653px">Login <svg width="7" height="6" viewBox="0 0 7 6"><path d="M0 3h6M4 1l2 2-2 2" stroke="#fecb35" fill="none"/></svg></div>
</header>
<nav class="sub-nav">
  <span style="left:243px">Fantasy</span>
  <span class="current" style="left:287px">Lobby</span>
  <span style="left:326px">Statistics</span>
  <span style="left:376px">Referral</span>
  <span style="left:421px">Mobile App</span>
  <span style="left:475px">Game Types</span>
</nav>

<div class="stadium" role="img" aria-label="Dark stadium field at night with gold field lines"></div>

<h1 class="page-title">LOBBY</h1>
<div class="countdown-label">NEXT CONTEST STARTS IN:</div>
<div class="count-box" style="left:318px">03</div>
<div class="colon" style="left:357px"><i></i><i></i></div>
<div class="count-box" style="left:366px">47</div>
<div class="colon" style="left:405px"><i></i><i></i></div>
<div class="count-box" style="left:414px">25</div>
<div class="create-btn">Create Contest <svg width="7" height="6" viewBox="0 0 7 6"><path d="M0 3h6M4 1l2 2-2 2" stroke="#fff" fill="none"/></svg></div>

<aside class="filter">
  <div class="filter-title">CONTEST FILTER</div>
  <div class="rule" style="top:47px"></div>
  <div class="search"><svg width="8" height="8" viewBox="0 0 8 8"><circle cx="3.3" cy="3.3" r="2.5" stroke="#fff" fill="none"/><path d="M5.2 5.2L7.5 7.5" stroke="#fff"/></svg>Search all Contests</div>
  <div class="chip-grid">
    <div class="chip">All Sports</div><div class="chip dim">AU Horse</div>
    <div class="chip">UK Horse</div><div class="chip dim">Racing 1</div>
    <div class="chip dim">Cage FC</div><div class="chip dim">Brawler</div>
    <div class="chip">Gridiron</div><div class="chip dim">Euro</div>
    <div class="chip on">Hoops</div><div class="chip dim">Diamond</div>
    <div class="chip">Ice League</div><div class="chip dim">African Cup</div>
    <div class="chip dim">World Cup</div><div class="chip">English</div>
    <div class="chip">Italian Serie</div><div class="chip">Spanish</div>
    <div class="chip dim">Euro Clubs</div><div class="chip">Friendly</div>
    <div class="chip dim">Euro</div><div class="chip">US Soccer</div>
    <div class="chip">German Top</div><div class="chip">Euro Clubs</div>
    <div class="chip">French Top</div><div class="chip">Pro Golf</div>
    <div class="chip">Super</div><div class="chip">Arena Esport</div>
  </div>
  <div class="rule" style="top:467px"></div>
  <div class="stack" style="top:484px">
    <div class="chip">All Start Types</div>
    <div class="chip on">Head To Head</div>
    <div class="chip">Leagues</div>
  </div>
  <div class="rule" style="top:580px"></div>
  <div class="fee-label">ENTRY FEE:</div>
  <div class="fee-input" style="left:14px">L00.0K</div>
  <div class="dash">-</div>
  <div class="fee-input" style="left:81px">L500</div>
  <svg class="slider" viewBox="0 0 128 14">
    <rect x="6" y="6" width="122" height="2" fill="#fff"/>
    <rect x="6" y="6" width="99" height="2" fill="#fecb35"/>
    <circle cx="7" cy="7" r="6.5" fill="#fff"/><path d="M6 4.5v5M8 4.5v5" stroke="#999" stroke-width=".7"/>
    <circle cx="105" cy="7" r="6.5" fill="#fff"/><path d="M104 4.5v5M106 4.5v5" stroke="#999" stroke-width=".7"/>
  </svg>
  <div class="rule" style="top:676px"></div>
  <div class="stack" style="top:693px">
    <div class="chip on">All Start Times</div>
    <div class="chip">Next Available</div>
    <div class="chip">Today</div>
  </div>
  <div class="rule" style="top:789px"></div>
  <div class="stack" style="top:807px">
    <div class="chip">All Creators</div>
    <div class="chip">Admin Created</div>
    <div class="chip on">User Created</div>
  </div>
</aside>

<section class="contests">
  <div class="th" style="left:18px"><span class="badge">M</span> Multi Entry</div>
  <div class="th" style="left:69px"><span class="badge">M</span> Multi Payout</div>
  <div class="th" style="left:126px"><span class="badge">G</span> Guaranteed</div>
  <div class="th" style="left:183px">Type</div>
  <div class="th" style="left:232px">Entries</div>
  <div class="th" style="left:262px">Entry</div>
  <div class="th" style="left:293px">Prizes</div>
  <div class="th" style="left:321px">Starts (EST)</div>
  <div class="head-rule"></div>
  <div class="rows">
    <div class="row" style="top:0"><svg width="9" height="9" viewBox="0 0 10 10"><circle cx="5" cy="5" r="4.3" fill="#fff" stroke="#222"/><circle cx="5" cy="5" r="1.6" fill="#222"/></svg><span class="name">Some long challenge name goes here</span><span style="left:165px">Player Draft</span><span style="left:214px">0/5</span><span style="left:244px">L0.00</span><span style="left:275px">L0</span><span style="left:303px">Sat Jan 20 9:30am</span><div class="btn" style="left:375px">Enter</div><div class="btn" style="left:413px">Invite</div></div>
    <div class="row" style="top:37.4px"><svg width="9" height="9" viewBox="0 0 10 10"><circle cx="5" cy="5" r="4.3" fill="#fff" stroke="#222"/><circle cx="5" cy="5" r="1.6" fill="#222"/></svg><span class="name">Some long challenge name goes here</span><span style="left:165px">Player Draft</span><span style="left:214px">0/5</span><span style="left:244px">L0.00</span><span style="left:275px">L0</span><span style="left:303px">Sat Jan 20 9:30am</span><div class="btn" style="left:375px">Enter</div><div class="btn" style="left:413px">Invite</div></div>
    <div class="row" style="top:74.8px"><svg width="9" height="9" viewBox="0 0 10 10"><circle cx="5" cy="5" r="4.3" fill="#fff" stroke="#222"/><circle cx="5" cy="5" r="1.6" fill="#222"/></svg><span class="name">Some long challenge name goes here</span><span style="left:165px">Player Draft</span><span style="left:214px">0/5</span><span style="left:244px">L0.00</span><span style="left:275px">L0</span><span style="left:303px">Sat Jan 20 9:30am</span><div class="btn" style="left:375px">Enter</div><div class="btn" style="left:413px">Invite</div></div>
    <div class="row" style="top:112.2px"><svg width="9" height="9" viewBox="0 0 10 10"><circle cx="5" cy="5" r="4.3" fill="#fff" stroke="#222"/><circle cx="5" cy="5" r="1.6" fill="#222"/></svg><span class="name">Some long challenge name goes here</span><span style="left:165px">Player Draft</span><span style="left:214px">0/5</span><span style="left:244px">L0.00</span><span style="left:275px">L0</span><span style="left:303px">Sat Jan 20 9:30am</span><div class="btn" style="left:375px">Enter</div><div class="btn" style="left:413px">Invite</div></div>
    <div class="row" style="top:149.6px"><svg width="9" height="9" viewBox="0 0 10 10"><ellipse cx="5" cy="5" rx="4.6" ry="3" transform="rotate(-35 5 5)" fill="#8b3a1e"/></svg><span class="name">Some long challenge name goes here</span><span style="left:165px">Player Draft</span><span style="left:214px">0/5</span><span style="left:244px">L0.00</span><span style="left:275px">L0</span><span style="left:303px">Sat Jan 20 9:30am</span><div class="btn" style="left:375px">Enter</div><div class="btn" style="left:413px">Invite</div></div>
    <div class="row" style="top:187px"><svg width="9" height="9" viewBox="0 0 10 10"><ellipse cx="5" cy="5" rx="4.6" ry="3" transform="rotate(-35 5 5)" fill="#8b3a1e"/></svg><span class="name">Some long challenge name goes here</span><span style="left:165px">Player Draft</span><span style="left:214px">5/5</span><span style="left:244px">L0.00</span><span style="left:275px">L0</span><span style="left:303px">Sat Jan 20 9:30am</span><div class="btn full" style="left:375px">Full</div><div class="btn" style="left:413px">Invite</div></div>
    <div class="row" style="top:224.4px"><svg width="9" height="9" viewBox="0 0 10 10"><ellipse cx="5" cy="5" rx="4.6" ry="3" transform="rotate(-35 5 5)" fill="#8b3a1e"/></svg><span class="name">Some long challenge name goes here</span><span style="left:165px">Player Draft</span><span style="left:214px">0/5</span><span style="left:244px">L0.00</span><span style="left:275px">L0</span><span style="left:303px">Sat Jan 20 9:30am</span><div class="btn" style="left:375px">Enter</div><div class="btn" style="left:413px">Invite</div></div>
    <div class="row" style="top:261.8px"><svg width="9" height="9" viewBox="0 0 10 10"><ellipse cx="5" cy="5" rx="4.6" ry="3" transform="rotate(-35 5 5)" fill="#8b3a1e"/></svg><span class="name">Some long challenge name goes here</span><span style="left:165px">Player Draft</span><span style="left:214px">0/5</span><span style="left:244px">L0.00</span><span style="left:275px">L0</span><span style="left:303px">Sat Jan 20 9:30am</span><div class="btn" style="left:375px">Enter</div><div class="btn" style="left:413px">Invite</div></div>
    <div class="row" style="top:299.2px"><svg width="9" height="9" viewBox="0 0 10 10"><ellipse cx="5" cy="5" rx="4.6" ry="3" transform="rotate(-35 5 5)" fill="#8b3a1e"/></svg><span class="name">Some long challenge name goes here</span><span style="left:165px">Player Draft</span><span style="left:214px">0/5</span><span style="left:244px">L0.00</span><span style="left:275px">L0</span><span style="left:303px">Sat Jan 20 9:30am</span><div class="btn" style="left:375px">Enter</div><div class="btn" style="left:413px">Invite</div></div>
    <div class="row" style="top:336.6px"><svg width="9" height="9" viewBox="0 0 10 10"><ellipse cx="5" cy="5" rx="4.6" ry="3" transform="rotate(-35 5 5)" fill="#8b3a1e"/></svg><span class="name">Some long challenge name goes here</span><span style="left:165px">Player Draft</span><span style="left:214px">0/5</span><span style="left:244px">L0.00</span><span style="left:275px">L0</span><span style="left:303px">Sat Jan 20 9:30am</span><div class="btn" style="left:375px">Enter</div><div class="btn" style="left:413px">Invite</div></div>
    <div class="row" style="top:374px"><svg width="9" height="9" viewBox="0 0 10 10"><ellipse cx="5" cy="5" rx="4.6" ry="3" transform="rotate(-35 5 5)" fill="#8b3a1e"/></svg><span class="name">Some long challenge name goes here</span><span style="left:165px">Player Draft</span><span style="left:214px">0/5</span><span style="left:244px">L0.00</span><span style="left:275px">L0</span><span style="left:303px">Sat Jan 20 9:30am</span><div class="btn" style="left:375px">Enter</div><div class="btn" style="left:413px">Invite</div></div>
    <div class="row" style="top:411.4px"><svg width="9" height="9" viewBox="0 0 10 10"><ellipse cx="5" cy="5" rx="4.6" ry="3" transform="rotate(-35 5 5)" fill="#8b3a1e"/></svg><span class="name">Some long challenge name goes here</span><span style="left:165px">Player Draft</span><span style="left:214px">0/5</span><span style="left:244px">L0.00</span><span style="left:275px">L0</span><span style="left:303px">Sat Jan 20 9:30am</span><div class="btn" style="left:375px">Enter</div><div class="btn" style="left:413px">Invite</div></div>
    <div class="row" style="top:448.8px"><svg width="9" height="9" viewBox="0 0 10 10"><ellipse cx="5" cy="5" rx="4.6" ry="3" transform="rotate(-35 5 5)" fill="#8b3a1e"/></svg><span class="name">Some long challenge name goes here</span><span style="left:165px">Player Draft</span><span style="left:214px">0/5</span><span style="left:244px">L0.00</span><span style="left:275px">L0</span><span style="left:303px">Sat Jan 20 9:30am</span><div class="btn" style="left:375px">Enter</div><div class="btn" style="left:413px">Invite</div></div>
    <div class="row" style="top:486.2px"><svg width="9" height="9" viewBox="0 0 10 10"><ellipse cx="5" cy="5" rx="4.6" ry="3" transform="rotate(-35 5 5)" fill="#8b3a1e"/></svg><span class="name">Some long challenge name goes here</span><span style="left:165px">Player Draft</span><span style="left:214px">0/5</span><span style="left:244px">L0.00</span><span style="left:275px">L0</span><span style="left:303px">Sat Jan 20 9:30am</span><div class="btn" style="left:375px">Enter</div><div class="btn" style="left:413px">Invite</div></div>
    <div class="row" style="top:523.6px"><svg width="9" height="9" viewBox="0 0 10 10"><circle cx="5" cy="5" r="4.3" fill="#fff" stroke="#3a6db0"/><path d="M2 6.5h6" stroke="#d9a21b" stroke-width="1.4"/></svg><span class="name">Some long challenge name goes here</span><span style="left:165px">Player Draft</span><span style="left:214px">0/5</span><span style="left:244px">L0.00</span><span style="left:275px">L0</span><span style="left:303px">Sat Jan 20 9:30am</span><div class="btn" style="left:375px">Enter</div><div class="btn" style="left:413px">Invite</div></div>
    <div class="row" style="top:561px"><svg width="9" height="9" viewBox="0 0 10 10"><circle cx="5" cy="5" r="4.3" fill="#fff" stroke="#3a6db0"/><path d="M2 6.5h6" stroke="#d9a21b" stroke-width="1.4"/></svg><span class="name">Some long challenge name goes here</span><span style="left:165px">Player Draft</span><span style="left:214px">0/5</span><span style="left:244px">L0.00</span><span style="left:275px">L0</span><span style="left:303px">Sat Jan 20 9:30am</span><div class="btn" style="left:375px">Enter</div><div class="btn" style="left:413px">Invite</div></div>
    <div class="row last" style="top:598.4px"><svg width="9" height="9" viewBox="0 0 10 10"><circle cx="5" cy="5" r="4.3" fill="#fff" stroke="#3a6db0"/><path d="M2 6.5h6" stroke="#d9a21b" stroke-width="1.4"/></svg><span class="name">Some long challenge name goes here</span><span style="left:165px">Player Draft</span><span style="left:214px">0/5</span><span style="left:244px">L0.00</span><span style="left:275px">L0</span><span style="left:303px">Sat Jan 20 9:30am</span><div class="btn" style="left:375px">Enter</div><div class="btn" style="left:413px">Invite</div></div>
  </div>
</section>

<div class="footer-rule"></div>
<footer class="footer">© 2018, ALL RIGHTS RESERVED.</footer>
</body>
</html>
```